Упаковка для Bright Vega
Задание на дизайн
Приоритеты объектов в упаковке
Зонтичная марка, Знак производителя, Марка продукта, Вид продукта, Название продукта, Иллюстрация
Размеры
Опишите свою организацию или продукт и целевую аудиторию
Производство и продажа электро-, бензо-, аккумуляторного инструмента для строительства и ремонта.
Существующая упаковка .То, что хочется обновить.
Образец существующей упаковки.
Комментарии и пожелания для дизайнеров
Необходимо полностью обновить устаревший дизайн упаковки для инструмента, на примере шуруповерта. Фирменный красный цвет, а также сам логотип и сочетания цветов внутри него менять нельзя. Логотип обязательно должен присутствовать на упаковке. Название серии Zet power line должно остаться, но в любом другом виде и написании. Остальное можно менять до неузнаваемости. Фото инструмента должно быть помещено на упаковку целиком. Упаковка должна быть современной, сочной, красочной, информативной и обязательно несложно адаптивной под другие виды инструмента и форматы коробок (ушм, перфораторы, лобзики и пр.). Другие образцы наших упаковок можно легко найти в сети.

```html
<!DOCTYPE html>
<html lang="en">
<head>
<meta charset="utf-8">
<title>Bright Vega — Drill Screwdriver Packaging</title>
<link rel="stylesheet" href="https://fonts.googleapis.com/css2?family=Barlow+Condensed:wght@500;600;700&family=Montserrat:wght@700;800&display=swap">
<style>
  :root {
    --brand-red: #d7261e;
    --ink-black: #1c1c1c;
    --panel-white: #f4f3f0;
    --text-dark: #151515;
    --text-light: #ffffff;
    --tool-red: #c8241c;
    --tool-black: #2a2a2a;
  }
  * { margin: 0; padding: 0; box-sizing: border-box; }
  html, body { width: 1200px; height: 1200px; overflow: hidden; background: var(--panel-white); }
  .box-front {
    position: relative;
    width: 1200px;
    height: 1200px;
    background: var(--panel-white);
    overflow: hidden;
  }
  .top-band {
    position: absolute;
    left: 0; top: 0;
    width: 1200px; height: 150px;
    background: var(--ink-black);
    display: flex;
  }
  .brand-block {
    width: 487px;
    height: 150px;
    background: var(--brand-red);
    display: flex;
    align-items: center;
    padding-left: 52px;
    font-family: "Montserrat", sans-serif;
    font-weight: 800;
    font-size: 52px;
    color: var(--text-light);
    letter-spacing: 0.5px;
  }
  .series-label {
    flex: 1;
    display: flex;
    align-items: center;
    justify-content: flex-end;
    padding-right: 52px;
    font-family: "Montserrat", sans-serif;
    font-weight: 800;
    font-size: 48px;
    color: var(--text-light);
    letter-spacing: 1px;
  }
  .product-type {
    position: absolute;
    left: 0; top: 150px;
    width: 487px; height: 505px;
    background: var(--ink-black);
    padding: 52px 0 0 52px;
    font-family: "Barlow Condensed", sans-serif;
    font-weight: 600;
    font-size: 140px;
    line-height: 124px;
    color: var(--text-light);
    text-transform: uppercase;
  }
  .tool-illustration {
    position: absolute;
    left: 530px; top: 200px;
    width: 620px; height: 940px;
    border-radius: 40px;
    background: linear-gradient(160deg, var(--tool-black) 0%, var(--tool-red) 45%, var(--tool-black) 100%);
  }
  .spec-list {
    position: absolute;
    left: 52px; top: 700px;
    list-style: none;
    font-family: "Barlow Condensed", sans-serif;
    font-weight: 600;
    color: var(--text-dark);
  }
  .spec-list li { font-size: 82px; line-height: 108px; }
  .spec-list li.spec-speed { font-size: 60px; letter-spacing: -0.5px; }
  .spec-list sup { font-size: 0.5em; vertical-align: 0.9em; }
</style>
</head>
<body>
  <main class="box-front">
    <header class="top-band">
      <div class="brand-block">BRIGHT VEGA</div>
      <div class="series-label">PROFESSIONAL</div>
    </header>

    <h1 class="product-type">Drill<br>Screw-<br>driver</h1>

    <div class="tool-illustration" role="img" aria-label="Red and black cordless drill screwdriver with Zet power line battery, shown whole"></div>

    <ul class="spec-list">
      <li class="spec-voltage">18 V</li>
      <li class="spec-torque">50 Nm</li>
      <li class="spec-speed">0-400 / 0-1500 min<sup>-1</sup></li>
      <li class="spec-chuck">13 mm</li>
    </ul>
  </main>
</body>
</html>
```